Talcum Powder Product Packaging - Brand Velvora Product Brisette

Talcum Powder Product packaging
Sophisticated Talcum Powder for Every Age
French Fragrance

Brand Name : Velvora
Product Name : Brisete
Product Pack : Measurement & Size Attached
Attached a Sample Product.

Looking for a Product Packaging for every age group.
Design Should be Aesthetic and Colorful . Target Market is all classes and all age group.

Target Market(s)

Upper Class

Industry/Entity Type

Product

Font styles to use
Decorative

Requirements
Must have
• Modern & Colorful - Use Dark Colors

```html
<!DOCTYPE html>
<html lang="en">
<head>
<meta charset="utf-8">
<title>Velvora Brisete — Sophisticated Talcum</title>
<link rel="stylesheet" href="https://fonts.googleapis.com/css2?family=Open+Sans:wght@400;600&family=Tinos:wght@400&family=Gelasio:wght@400&display=swap">
<style>
  :root {
    --wine-deep: #6e0a0e;
    --wine: #8e1416;
    --crimson: #b3261e;
    --coral: #e0563f;
    --peach: #f6a88c;
    --glow: #fff1ea;
    --ink-dark: #2a0d0b;
    --brand-red: #c8193a;
    --band-white: #f3e6e2;
  }
  * { margin: 0; padding: 0; box-sizing: border-box; }
  html, body { width: 1200px; height: 834px; overflow: hidden; background: #ffffff; }
  .pack-face {
    position: relative;
    width: 1200px;
    height: 834px;
    overflow: hidden;
    background:
      radial-gradient(ellipse 520px 480px at 830px 470px, var(--peach) 0%, var(--coral) 40%, rgba(179,38,30,0) 85%),
      linear-gradient(90deg, var(--wine-deep) 0%, var(--wine) 35%, var(--crimson) 70%, var(--coral) 100%);
  }
  .border-band {
    position: absolute;
    left: 84px;
    width: 1044px;
    background: var(--band-white);
    opacity: 0.9;
  }
  .border-band--top { top: 22px; height: 22px; }
  .border-band--bottom { top: 787px; height: 16px; }
  .base-strip {
    position: absolute;
    left: 84px;
    top: 816px;
    width: 1044px;
    height: 18px;
    background: var(--wine-deep);
  }
  .lotus-art {
    position: absolute;
    left: 600px;
    top: 150px;
    width: 500px;
    height: 570px;
    background: radial-gradient(ellipse 50% 55% at 50% 62%, var(--glow) 0%, rgba(255,230,220,0.75) 40%, rgba(246,168,140,0) 80%);
  }
  .brand-name {
    position: absolute;
    left: 628px;
    width: 400px;
    top: 456px;
    text-align: center;
    font-family: "Tinos", "Times New Roman", serif;
    font-size: 20px;
    letter-spacing: 0.5px;
    color: var(--ink-dark);
  }
  .product-name {
    position: absolute;
    left: 578px;
    width: 500px;
    top: 500px;
    text-align: center;
    font-family: "Open Sans", Arial, sans-serif;
    font-weight: 400;
    font-size: 82px;
    line-height: 1;
    letter-spacing: 2px;
    color: var(--brand-red);
  }
  .product-type {
    position: absolute;
    left: 678px;
    width: 300px;
    top: 584px;
    text-align: center;
    font-family: "Open Sans", Arial, sans-serif;
    font-size: 16px;
    color: var(--ink-dark);
  }
  .tagline {
    position: absolute;
    left: 662px;
    width: 400px;
    top: 742px;
    text-align: center;
    font-family: "Gelasio", Georgia, serif;
    font-size: 18px;
    color: var(--ink-dark);
  }
</style>
</head>
<body>
  <main class="pack-face">
    <div class="border-band border-band--top" role="img" aria-label="White ornamental border pattern"></div>
    <div class="lotus-art" role="img" aria-label="Glowing white lotus flower with rising sparkles and reflection"></div>
    <p class="brand-name">VELVORA<sup style="font-size:8px;">®</sup></p>
    <h1 class="product-name">BRISETE</h1>
    <p class="product-type">Sophisticated Talcum</p>
    <p class="tagline">Powder for Every Age French Fragrance</p>
    <div class="border-band border-band--bottom" role="img" aria-label="White ornamental border pattern"></div>
    <div class="base-strip"></div>
  </main>
</body>
</html>
```